New corporate Powerpoint template *

Hi,
We would like to have one new corporate Powerpoint template which can be used for various presentations (Sales, Investors, Marketing, Engineers, HR, Corporate presentations…) Please note that this template will be used for both internal and external presentations.
Please take a look at our website to get a feel for our branding.
https://www.brenvar-microtech.example/

Some visual elements to include:

• The theme needs to be relevant to our industry i.e. Semiconductor theme (circuit board/chip graphic elements)
• Simple uses of color, lifestyle images, moving away from Geometric patterns and colorful wave
• Style should be modern, clean and gender neutral
• Use Korvet blue as more of an accent color - Avoid the overuse of blue (seems a little too bright sometimes)
• Korvet logo to appear on every page

Necessary slides to include:
• Cover Slide
• Agenda Slide
• Divider / Title Slide
• Content Slide
• White Slide
• Comparison slide (two, three, four)
• Table slide with the ability to add rows/columns
• Timeline/roadmap slide
• End Slide

Target Market(s)

Semiconductor industry

Font styles to use
Other font styles liked:
• Arial or Rockwell

Colors
33a6d7

Requirements
Must have
• • The theme needs to be relevant to our industry i.e. Semiconductor theme (circuit board/chip graphic elements)
• • Simple uses of color, lifestyle images
• • Style should be modern, clean and gender neutral
• • Use Korvet blue as more of an accent color
• • Korvet logo to appear on every page
• Necessary slides to include:
• • Cover Slide
• • Agenda Slide
• • Divider / Title Slide
• • Content Slide
• • White Slide
• • Comparison slide (two, three, four)
• • Table slide with the ability to add rows/columns
• • Timeline/roadmap slide
• • End Slide
Nice to have
Should not have
• - Avoid the overuse of blue (seems a little too bright sometimes)
• - Do not use any kind of wave as a graphic

```html
<!DOCTYPE html>
<html lang="en">
<head>
<meta charset="utf-8">
<title>Korvet Corporate Presentation Template</title>
<link href="https://fonts.googleapis.com/css2?family=Arvo:wght@400;700&family=Arimo:wght@400;700&display=swap" rel="stylesheet">
<style>
:root{
  --blue:#33a6d7;
  --blue-deep:#1f78c0;
  --violet:#5a62c9;
  --orange:#f28a1d;
  --ink:#2b2b2b;
  --grey:#666;
  --rule:#dde3ea;
  --row:#f3f6f9;
  --stage-light:#ececec;
  --stage-dark:#3b3b3b;
  --white:#fff;
  --lilac:#e6e3f4;
}
*{box-sizing:border-box;margin:0;padding:0}
html,body{width:1200px;height:2497px;overflow:hidden}
body{background:var(--stage-dark);font-family:"Arimo",Arial,sans-serif;color:var(--ink);position:relative}
.stage-top{position:absolute;left:0;top:0;width:1200px;height:727px;background:var(--stage-light)}
.slide{position:absolute;background:var(--white);overflow:hidden;box-shadow:0 8px 18px rgba(0,0,0,.35)}
.slide.small{width:519px;height:292px}
.hero{left:150px;top:90px;width:900px;height:506px;box-shadow:0 6px 24px rgba(0,0,0,.18)}
.abs{position:absolute}
.wordmark{position:absolute;display:flex;align-items:center;font-family:"Arvo",Georgia,serif;font-weight:700;color:var(--blue);white-space:nowrap}
.wordmark .dot{border-radius:50%;background:var(--blue);margin-right:.25em}
.wordmark.light{color:var(--white)}
.wordmark.light .dot{background:var(--white)}
.wm-s{font-size:20px}.wm-s .dot{width:14px;height:14px}
.wm-l{font-size:52px}.wm-l .dot{width:38px;height:38px}
.title{font-family:"Arvo",Georgia,serif;font-weight:700;color:var(--blue);line-height:1.1;white-space:nowrap}
.subtitle{font-family:"Arvo",Georgia,serif;color:#555;line-height:1.15;white-space:nowrap}
.slide-head{font-family:"Arvo",Georgia,serif;font-weight:700;font-size:15px;line-height:1}
.sub-head{font-size:6.5px;color:var(--grey);margin-top:3px}
.copy{font-size:5.4px;line-height:1.45;color:#555}
.copy.strong{font-weight:700;color:var(--ink);font-size:6.3px;font-family:"Arvo",Georgia,serif}
.item-title{font-family:"Arvo",Georgia,serif;font-weight:700;font-size:6.4px;color:var(--ink)}
.orange{color:var(--orange)}
.num{position:absolute;width:18px;height:18px;border-radius:50%;background:var(--orange);color:#fff;font-size:7px;display:flex;align-items:center;justify-content:center;font-weight:700}
.num.outline{background:none;border:1px solid rgba(255,255,255,.8)}
.num.outline-o{background:var(--white);border:1px solid var(--orange);color:var(--orange)}
.photo{position:absolute}
.lilac-tab{position:absolute;right:0;top:0;width:250px;height:52px;background:var(--lilac);border-bottom-left-radius:28px}
.ico{position:absolute;width:12px;height:12px}
.contact-row{display:flex;align-items:flex-start;gap:5px;font-size:6px;color:#444;margin-top:5px;line-height:1.35}
.contact-row svg{flex:none;width:8px;height:8px;margin-top:1px}
.data-table{position:absolute;left:20px;top:78px;width:479px;border-collapse:collapse;font-size:6px}
.data-table th{background:var(--blue);color:#fff;font-family:"Arvo",Georgia,serif;font-weight:700;text-align:left;padding:6px 8px}
.data-table td{padding:6px 8px;color:#555;border-bottom:1px solid var(--rule)}
.data-table tr:nth-child(even) td{background:var(--row)}
.compare-card{position:absolute;top:88px;width:222px;height:170px;border:1px solid var(--rule);border-radius:6px;padding:12px 14px}
.compare-card .bar{height:3px;width:34px;background:var(--orange);margin:5px 0 8px}
.compare-card li{list-style:none;font-size:5.6px;color:#555;line-height:1.45;margin-bottom:5px;display:flex;gap:5px}
.compare-card li::before{content:"";flex:none;width:4px;height:4px;border-radius:50%;background:var(--blue);margin-top:2px}
.timeline-line{position:absolute;left:40px;top:168px;width:440px;height:2px;background:var(--rule)}
.milestone{position:absolute;width:100px;text-align:center}
.milestone .year{font-family:"Arvo",Georgia,serif;font-weight:700;font-size:9px;color:var(--blue)}
</style>
</head>
<body>

<div class="stage-top"></div>

<!-- Featured cover -->
<section class="slide hero">
  <svg class="abs" width="900" height="506" viewBox="0 0 900 506" aria-hidden="true">
    <defs>
      <linearGradient id="coverPhoto" x1="0" y1="0" x2="1" y2="1">
        <stop offset="0" stop-color="#2a2f4a"/><stop offset=".55" stop-color="#4a3b55"/><stop offset="1" stop-color="#c9a27a"/>
      </linearGradient>
    </defs>
    <path d="M265 0 H900 V370 H635 Z" fill="url(#coverPhoto)" role="img" aria-label="Photo of three engineers studying data on a screen in a dark office"/>
    <path d="M245 10 L615 385 H900" fill="none" stroke="var(--blue)" stroke-width="8"/>
  </svg>
  <div class="wordmark wm-l" style="left:50px;top:170px"><span class="dot"></span>Korvet</div>
  <h1 class="title abs" style="left:50px;top:300px;font-size:42px">Powering the Smart<br>Connected Future</h1>
  <p class="subtitle abs" style="left:50px;top:405px;font-size:19px">Transforming analog fundamentals into power efficient,<br>connected solutions</p>
</section>

<!-- Cover A -->
<section class="slide small" style="left:50px;top:779px">
  <svg class="abs" width="519" height="292" viewBox="0 0 519 292" aria-hidden="true">
    <defs>
      <linearGradient id="coverA" x1="0" y1="0" x2="1" y2="1">
        <stop offset="0" stop-color="#2a2f4a"/><stop offset=".55" stop-color="#4a3b55"/><stop offset="1" stop-color="#c9a27a"/>
      </linearGradient>
    </defs>
    <path d="M160 0 H519 V212 H370 Z" fill="url(#coverA)" role="img" aria-label="Photo of three engineers studying data on a screen"/>
    <path d="M150 6 L362 222 H519" fill="none" stroke="var(--blue)" stroke-width="5"/>
  </svg>
  <div class="wordmark" style="left:30px;top:100px;font-size:30px"><span class="dot" style="width:22px;height:22px"></span>Korvet</div>
  <h2 class="title abs" style="left:30px;top:165px;font-size:22px">Powering the Smart<br>Connected Future</h2>
  <p class="subtitle abs" style="left:30px;top:232px;font-size:10.5px">Transforming analog fundamentals into power efficient,<br>connected solutions</p>
</section>

<!-- Cover B -->
<section class="slide small" style="left:622px;top:779px">
  <svg class="abs" width="519" height="292" viewBox="0 0 519 292" aria-hidden="true">
    <defs>
      <linearGradient id="coverB" x1="0" y1="0" x2="1" y2="1">
        <stop offset="0" stop-color="#1f2440"/><stop offset=".6" stop-color="#3c3350"/><stop offset="1" stop-color="#a98c72"/>
      </linearGradient>
    </defs>
    <path d="M262 0 H519 V292 H342 Z" fill="url(#coverB)" role="img" aria-label="Photo of engineers reviewing charts on a display"/>
    <path d="M250 0 L330 292" fill="none" stroke="var(--blue)" stroke-width="5"/>
  </svg>
  <div class="wordmark" style="left:28px;top:75px;font-size:26px"><span class="dot" style="width:19px;height:19px"></span>Korvet</div>
  <h2 class="title abs" style="left:28px;top:135px;font-size:19px">Powering the Smart<br>Connected Future</h2>
  <p class="subtitle abs" style="left:28px;top:186px;font-size:9.5px">Transforming analog fundamentals<br>into power efficient, connected solutions</p>
</section>

<!-- Agenda -->
<section class="slide small" style="left:50px;top:1118px">
  <svg class="abs" width="519" height="292" viewBox="0 0 519 292" aria-hidden="true">
    <defs>
      <linearGradient id="agendaBand" x1="0" y1="0" x2="1" y2="0">
        <stop offset="0" stop-color="var(--blue)"/><stop offset="1" stop-color="var(--violet)"/>
      </linearGradient>
    </defs>
    <path d="M0 0 H400 V40 Q400 64 376 64 H0 Z" fill="url(#agendaBand)"/>
  </svg>
  <div class="abs" style="left:30px;top:22px;color:#fff"><div class="slide-head">Our Agenda</div><div class="sub-head" style="color:#e8f4fb">Sub Heading goes here</div></div>
  <div class="wordmark wm-s" style="right:18px;top:18px"><span class="dot"></span>Korvet</div>
  <div class="photo" role="img" aria-label="Photo of business colleagues discussing documents at a desk" style="left:0;top:72px;width:245px;height:176px;border-radius:0 26px 26px 0;background:linear-gradient(135deg,#e9e4dc,#b9a892 60%,#4a4f63)"></div>
  <div class="num" style="left:236px;top:100px">01</div>
  <div class="num" style="left:236px;top:150px">02</div>
  <div class="num" style="left:236px;top:200px">03</div>
  <div class="abs" style="left:265px;top:100px;width:200px"><div class="item-title">YOU TEXT HERE</div><p class="copy">Sample text for the first agenda point and its topic.</p></div>
  <div class="abs" style="left:265px;top:150px;width:200px"><div class="item-title">YOU TEXT HERE</div><p class="copy">Sample text for the second agenda point and its topic.</p></div>
  <div class="abs" style="left:265px;top:200px;width:200px"><div class="item-title">YOU TEXT HERE</div><p class="copy">Sample text for the third agenda point and its topic.</p></div>
</section>

<!-- Divider -->
<section class="slide small" style="left:622px;top:1118px;background:linear-gradient(120deg,var(--blue) 0%,#2d8fd0 45%,var(--violet) 100%)">
  <div class="photo" role="img" aria-label="Photo of a businessman in a suit" style="right:0;top:0;width:120px;height:110px;background:linear-gradient(160deg,#d9dde6,#5b6482)"></div>
  <div class="wordmark wm-s light" style="left:240px;top:16px"><span class="dot"></span>Korvet</div>
  <div class="num outline" style="left:20px;top:95px">01</div>
  <div class="num outline" style="left:20px;top:145px">02</div>
  <div class="num outline" style="left:20px;top:195px">03</div>
  <p class="copy abs" style="left:50px;top:92px;width:140px;color:#eaf5fc">Sample text for the first point of this section goes here in short.</p>
  <p class="copy abs" style="left:50px;top:142px;width:140px;color:#eaf5fc">Sample text for the second point of this section goes here in short.</p>
  <p class="copy abs" style="left:50px;top:192px;width:140px;color:#eaf5fc">Sample text for the third point of this section goes here in short.</p>
  <div class="photo" role="img" aria-label="Photo of a seated professional" style="left:290px;top:230px;width:229px;height:62px;background:linear-gradient(90deg,#4b5470,#20273d)"></div>
  <div class="abs" style="left:228px;top:110px;width:265px;height:120px;background:#fff;border-radius:8px">
    <div class="abs" style="left:20px;top:32px;width:110px"><div class="item-title">YOU TEXT HERE</div><p class="copy">Sample text that explains this divider topic in a few short lines.</p></div>
    <div class="photo" role="img" aria-label="Photo of a man working on a laptop" style="left:145px;top:10px;width:112px;height:100px;border-radius:6px;background:linear-gradient(150deg,#e7e9ee,#8e97a8)"></div>
  </div>
</section>

<!-- Title / features -->
<section class="slide small" style="left:50px;top:1458px">
  <div class="photo" role="img" aria-label="Photo of an older couple walking with a bicycle, tinted orange" style="left:0;top:0;width:185px;height:292px;border-radius:0 24px 24px 0;background:linear-gradient(180deg,#f39a2c,#e7791a)"></div>
  <div class="abs" style="left:20px;top:22px;color:#fff"><div class="slide-head">Title Text</div><div class="sub-head" style="color:#fde9d3">Sub Heading goes here</div></div>
  <div class="wordmark wm-s" style="right:18px;top:18px"><span class="dot"></span>Korvet</div>
  <p class="copy abs" style="left:220px;top:70px;width:280px">Sample text for this title slide, a short line that states the main message of the section in brief and sets up the points below.</p>
  <svg class="ico" style="left:220px;top:125px" viewBox="0 0 12 12" aria-hidden="true"><rect x="2" y="1" width="8" height="10" rx="1" fill="none" stroke="var(--blue)"/><path d="M4 4h4M4 6h4M4 8h3" stroke="var(--blue)"/></svg>
  <svg class="ico" style="left:370px;top:125px" viewBox="0 0 12 12" aria-hidden="true"><path d="M6 10 L1.5 5.5 A2.3 2.3 0 0 1 6 3 A2.3 2.3 0 0 1 10.5 5.5 Z" fill="none" stroke="var(--blue)"/></svg>
  <svg class="ico" style="left:220px;top:195px" viewBox="0 0 12 12" aria-hidden="true"><path d="M3 1h6v3a3 3 0 0 1-6 0z M6 7v3 M4 11h4" fill="none" stroke="var(--blue)"/></svg>
  <svg class="ico" style="left:370px;top:195px" viewBox="0 0 12 12" aria-hidden="true"><circle cx="6" cy="6.5" r="4.5" fill="none" stroke="var(--blue)"/><path d="M6 4v3h2" stroke="var(--blue)" fill="none"/></svg>
  <div class="abs" style="left:220px;top:145px;width:120px"><div class="item-title" style="color:var(--blue)">YOU TEXT HERE</div><p class="copy">Sample text for this point goes here.</p></div>
  <div class="abs" style="left:370px;top:145px;width:120px"><div class="item-title" style="color:var(--blue)">YOU TEXT HERE</div><p class="copy">Sample text for this point goes here.</p></div>
  <div class="abs" style="left:220px;top:215px;width:120px"><div class="item-title" style="color:var(--blue)">YOU TEXT HERE</div><p class="copy">Sample text for this point goes here.</p></div>
  <div class="abs" style="left:370px;top:215px;width:120px"><div class="item-title" style="color:var(--blue)">YOU TEXT HERE</div><p class="copy">Sample text for this point goes here.</p></div>
</section>

<!-- About -->
<section class="slide small" style="left:622px;top:1458px">
  <div class="abs" style="left:20px;top:16px"><div class="slide-head">About Our Company</div><div class="sub-head">Sub Heading goes here</div></div>
  <div class="wordmark wm-s" style="right:18px;top:18px"><span class="dot"></span>Korvet</div>
  <div class="photo" role="img" aria-label="Close-up photo of a green circuit board with chips" style="left:0;top:75px;width:270px;height:150px;border-radius:0 75px 75px 0;background:linear-gradient(135deg,#1f5a45,#2d7a5a 50%,#153b2f)"></div>
  <div class="abs" style="left:300px;top:80px;width:200px">
    <div class="item-title" style="font-size:9px">Korvet</div>
    <p class="copy" style="margin-top:6px">We are a fabless microtech company focused on highly integrated mixed-signal products for consumer electronics. Our passion for innovation drives us to make power efficient, connected devices that serve people in everyday life and in industry.</p>
  </div>
  <svg class="abs" style="left:300px;top:200px;width:12px;height:12px" viewBox="0 0 12 12" aria-hidden="true"><circle cx="6" cy="6" r="6" fill="var(--orange)"/></svg>
  <svg class="abs" style="left:300px;top:230px;width:12px;height:12px" viewBox="0 0 12 12" aria-hidden="true"><circle cx="6" cy="6" r="6" fill="var(--orange)"/></svg>
  <div class="abs" style="left:320px;top:199px;width:170px"><div class="item-title">YOU TEXT HERE</div><p class="copy">Sample text for this point goes here.</p></div>
  <div class="abs" style="left:320px;top:229px;width:170px"><div class="item-title">YOU TEXT HERE</div><p class="copy">Sample text for this point goes here.</p></div>
</section>

<!-- Table slide -->
<section class="slide small" style="left:50px;top:1797px">
  <div class="lilac-tab"></div>
  <div class="abs" style="left:20px;top:16px"><div class="slide-head" style="color:var(--blue)">Table Slide</div><div class="sub-head">Sub Heading goes here</div></div>
  <div class="wordmark wm-s" style="right:18px;top:18px"><span class="dot"></span>Korvet</div>
  <p class="copy strong abs" style="left:20px;top:62px">Lorem Ipsum is simply dummy text of the printing and typesetting industry.</p>
  <table class="data-table">
    <thead><tr><th>Product</th><th>Segment</th><th>Status</th><th>Launch</th></tr></thead>
    <tbody>
      <tr><td>Power unit A</td><td>Mobile</td><td>In market</td><td>Q1</td></tr>
      <tr><td>Power unit B</td><td>Wearables</td><td>Sampling</td><td>Q2</td></tr>
      <tr><td>Radio chip C</td><td>IoT</td><td>In design</td><td>Q3</td></tr>
      <tr><td>Charger D</td><td>Automotive</td><td>Planned</td><td>Q4</td></tr>
      <tr><td>Sensor hub E</td><td>Industrial</td><td>Planned</td><td>Q4</td></tr>
    </tbody>
  </table>
</section>

<!-- Comparison slide -->
<section class="slide small" style="left:622px;top:1797px">
  <div class="lilac-tab"></div>
  <div class="abs" style="left:20px;top:16px"><div class="slide-head" style="color:var(--blue)">Comparison Slide</div><div class="sub-head">Sub Heading goes here</div></div>
  <div class="wordmark wm-s" style="right:18px;top:18px"><span class="dot"></span>Korvet</div>
  <p class="copy strong abs" style="left:20px;top:62px">Lorem Ipsum is simply dummy text of the printing and typesetting industry.</p>
  <div class="compare-card" style="left:20px">
    <div class="item-title" style="font-size:8px">Option One</div><div class="bar"></div>
    <ul>
      <li>Sample point that describes a key feature of this option.</li>
      <li>Sample point that describes a key benefit of this option.</li>
      <li>Sample point that describes cost and timing.</li>
      <li>Sample point that describes the main risk.</li>
    </ul>
  </div>
  <div class="compare-card" style="left:277px">
    <div class="item-title" style="font-size:8px">Option Two</div><div class="bar"></div>
    <ul>
      <li>Sample point that describes a key feature of this option.</li>
      <li>Sample point that describes a key benefit of this option.</li>
      <li>Sample point that describes cost and timing.</li>
      <li>Sample point that describes the main risk.</li>
    </ul>
  </div>
</section>

<!-- Timeline slide -->
<section class="slide small" style="left:50px;top:2137px">
  <div class="lilac-tab"></div>
  <div class="abs" style="left:20px;top:16px"><div class="slide-head" style="color:var(--blue)">Roadmap Slide</div><div class="sub-head">Sub Heading goes here</div></div>
  <div class="wordmark wm-s" style="right:18px;top:18px"><span class="dot"></span>Korvet</div>
  <p class="copy strong abs" style="left:20px;top:62px">Lorem Ipsum is simply dummy text of the printing and typesetting industry.</p>
  <div class="timeline-line"></div>
  <div class="num outline-o" style="left:61px;top:160px">01</div>
  <div class="num outline-o" style="left:181px;top:160px">02</div>
  <div class="num outline-o" style="left:301px;top:160px">03</div>
  <div class="num outline-o" style="left:421px;top:160px">04</div>
  <div class="milestone" style="left:20px;top:115px"><div class="year">2024</div><div class="item-title orange">YOU TEXT HERE</div></div>
  <div class="milestone" style="left:140px;top:115px"><div class="year">2025</div><div class="item-title orange">YOU TEXT HERE</div></div>
  <div class="milestone" style="left:260px;top:115px"><div class="year">2026</div><div class="item-title orange">YOU TEXT HERE</div></div>
  <div class="milestone" style="left:380px;top:115px"><div class="year">2027</div><div class="item-title orange">YOU TEXT HERE</div></div>
  <p class="copy milestone" style="left:20px;top:192px">Sample text for this stage of the roadmap.</p>
  <p class="copy milestone" style="left:140px;top:192px">Sample text for this stage of the roadmap.</p>
  <p class="copy milestone" style="left:260px;top:192px">Sample text for this stage of the roadmap.</p>
  <p class="copy milestone" style="left:380px;top:192px">Sample text for this stage of the roadmap.</p>
</section>

<!-- End slide -->
<section class="slide small" style="left:622px;top:2137px">
  <div class="photo" role="img" aria-label="Street map showing the location of the company headquarters" style="left:0;top:0;width:290px;height:292px;background:linear-gradient(135deg,#eef0ec,#dfe6df 50%,#cfe3ef)"></div>
  <svg class="abs" style="left:130px;top:78px;width:16px;height:22px" viewBox="0 0 16 22" aria-hidden="true"><path d="M8 22 C3 14 0 11 0 8 A8 8 0 0 1 16 8 C16 11 13 14 8 22Z" fill="#e53935"/><circle cx="8" cy="8" r="3" fill="#fff"/></svg>
  <div class="wordmark" style="left:315px;top:75px;font-size:24px"><span class="dot" style="width:17px;height:17px"></span>Korvet</div>
  <div class="abs" style="left:315px;top:125px;width:195px">
    <div class="item-title" style="font-size:10px">Thank you</div>
    <p class="copy" style="font-weight:700;margin-top:4px;color:#333">The address of our corporate headquarters is:</p>
    <div class="contact-row"><svg viewBox="0 0 8 8" aria-hidden="true"><path d="M4 8 C2 5 1 4 1 3 A3 3 0 0 1 7 3 C7 4 6 5 4 8Z" fill="var(--blue)"/></svg><span>12 Harlow Quay<br>Fenmoor Park<br>Eastbridge EB4 7QX<br>United Kingdom</span></div>
    <div class="contact-row"><svg viewBox="0 0 8 8" aria-hidden="true"><rect x="0.5" y="1.5" width="7" height="5" fill="none" stroke="var(--blue)"/><path d="M0.5 1.5 L4 4.5 L7.5 1.5" fill="none" stroke="var(--blue)"/></svg><span>info@brenvar-microtech.example</span></div>
    <div class="contact-row"><svg viewBox="0 0 8 8" aria-hidden="true"><path d="M1.5 0.5 L3 2.5 L2 3.5 C2.6 4.8 3.4 5.6 4.5 6 L5.5 5 L7.5 6.5 L6.5 7.5 C3.5 7.5 0.5 4.5 0.5 1.5Z" fill="var(--blue)"/></svg><span>+44 (0) 1000 555 010</span></div>
    <div class="contact-row"><svg viewBox="0 0 8 8" aria-hidden="true"><circle cx="4" cy="4" r="3.5" fill="none" stroke="var(--blue)"/><path d="M0.5 4h7M4 0.5c-2 2-2 5 0 7M4 0.5c2 2 2 5 0 7" fill="none" stroke="var(--blue)" stroke-width=".6"/></svg><span>www.brenvar-microtech.example</span></div>
  </div>
</section>

</body>
</html>
```